CD cover Digipack For Singer & Songwriter

I need a Full Digipack CD cover without booklet, for my first album.

My Name is Marek Dulane and Im a Pastor and a singer & songwriter based in berlin.
All of the music is Christian/Gospel music, and has a soul flare to it. It is a unplugged/acoustic album.

It will be available to download from the label web shop as well as a limited physical release.

The title of the album is "Open the Gate" and should be included on the cover and CD image.

The following information must be included in the Digipack.

Here are the tracks, this is the final order.

Tracks:

1 Cold River
2 Paper Lanterns
3 Bread Upon the Water (Feat. Valmek)
4 Open the Gate (Feat. Dax Orrin)
5 Carry the Bell
6 Over the Broken Hill
7 Slow Dawn
8 Verwandelt
9 Zum Ufer

On the inside of the Digipack I would like to have a short Bio (attached in the documents) you can format the content how you like.

I also need to include this information somewhere, I'll leave it up to you where to put it:

Recorded at Quill Records in Berlin

Copyright ©2017 Quill Records
www.quill-records.net

Marek Dulane
www.marekdulane.net

Please also include all the documents attached to the Digipack:
Label name, label code etc...

Look And Feel: Elegant, Modern...

Target Market(s)

Christian Gospel / Unplugged Acoustic

Industry/Entity Type

Singer

Font styles to use
Serif
Sans Serif
Decorative
Script

Colors
ffffff

Requirements
Must have
• 1 Cold River (03:25)
• 2 Paper Lanterns (02:44)
• 3 Bread Upon the Water (Feat. Valmek) (03:23)
• 4 Open the Gate (Feat. Dax Orrin) (03.01)
• 5 Carry the Bell (03:27)
• 6 Over the Broken Hill (03:00)
• 7 Slow Dawn (03:35)
• 8 Verwandelt (03:40)
• 9 Zum Ufer (04:11)
• CD-Duration 29:06 minutes
• QR 58273
• On the inside of the Digipack I would like to have a short Bio (attached in the documents) you can format the content how you like.
• I also need to include this information somewhere, I'll leave it up to you where to put it:
• Recorded at Quill Records in Berlin
• Copyright ©2017 Quill Records
• www.quillrecords.net
• Marek Dulane
• www.marekdulane.net
• Please also include all the documents attached to the Digipack:
• Label name, label code etc...

```html
<!DOCTYPE html>
<html lang="en">
<head>
<meta charset="utf-8">
<title>Open the Gate – Bio Panel</title>
<link rel="stylesheet" href="https://fonts.googleapis.com/css2?family=Parisienne&display=swap">
<style>
  :root {
    --paper: #ffffff;
    --haze: #eceef2;
    --ink: #141414;
    --suit: rgba(78, 84, 96, 0.9);
    --suit-soft: rgba(140, 144, 154, 0.45);
    --wood: rgba(170, 110, 60, 0.55);
  }
  html, body {
    margin: 0;
    padding: 0;
    width: 1200px;
    height: 1200px;
    overflow: hidden;
    background: var(--paper);
  }
  .panel {
    position: relative;
    width: 1200px;
    height: 1200px;
    background: linear-gradient(100deg, var(--haze) 0%, var(--paper) 60%);
    overflow: hidden;
  }
  .artist-photo {
    position: absolute;
    left: 0;
    top: 190px;
    width: 760px;
    height: 1010px;
    background:
      radial-gradient(ellipse 26% 14% at 34% 56%, var(--wood), transparent 100%),
      radial-gradient(ellipse 60% 55% at 28% 60%, var(--suit), var(--suit-soft) 55%, transparent 80%);
  }
  .bio {
    position: absolute;
    right: 38px;
    top: 128px;
    width: 760px;
    text-align: right;
    font-family: "Parisienne", cursive;
    font-size: 27px;
    line-height: 40px;
    color: var(--ink);
  }
  .bio-title {
    margin: 0 0 38px;
    font-size: 27px;
    font-weight: 400;
  }
  .bio-paragraph {
    margin: 0 0 40px;
  }
  .bio-paragraph span {
    display: block;
  }
</style>
</head>
<body>
  <main class="panel">
    <div class="artist-photo" role="img" aria-label="Photograph of the artist in a grey suit seated, playing an acoustic guitar, fading into white"></div>

    <section class="bio">
      <h1 class="bio-title">A brief chronicle of my life.</h1>
      <p class="bio-paragraph">
        <span>My origin can be traced back to the north of Brazil - a</span>
        <span>warm, homely, simple pastoral region from which I moved</span>
        <span>away in 2007 to Germany. Berlin welcomed me with open</span>
        <span>arms and quickly became my new home. My love affair with</span>
        <span>music began at quiet an early age too. I started learning to</span>
        <span>play the guitar at age 12. Teaching myself to play the oh, so</span>
        <span>loved instrument and staying dedicated to the craft.</span>
        <span>Once I began playing in the church by 14, my love for music</span>
        <span>became so ingrained in me that I never stopped.</span>
      </p>
      <p class="bio-paragraph">
        <span>The church is home to me. In my heart I know my gift is of</span>
        <span>the Lord and its purpose is to do his work. I have been mar-</span>
        <span>ried since 2015 and I am a father of one - an amazingly</span>
        <span>beautiful daughter, whose life has made me my calling to</span>
        <span>serve the Lord even stronger. A path which led me to becom-</span>
        <span>ing a pastor at Evangelische Gemeinde Lichtweg</span>
        <span>e.V.; where I preach and lead in praise and</span>
        <span>worship. Praising God is joy. Praising God is music.</span>
        <span>Praising God is a calling. So, do feel welcome to praise.</span>
        <span>Welcome to my world … and feel inspired!</span>
      </p>
    </section>
  </main>
</body>
</html>
```